Motor Vault Website - Part of the Brantley Group

A complimentary website is required for the launch of a 'Motor Vault' - a new service launched by industry renowned BRANTLEY. Motor Vault is an industry-first brand that designs and builds unique subterranean car parks for private residential homes in London and the influential counties within the UK. Please see here the direction of a new BRANTLEY Website - we would like Motor Vault to be complimentary and sit alongside BRANTLEY harmoniously - https://www.brantleyhq.example/brantley-nu-staging Brantley have some images, but whilst more professional images are in production - we have also attached pixmoor photos- named clearly as pixmoor. **Attached files include JPEG, .eps of logo and Brantley library images and Pixmoor Library Images - two versions of logo dependent on background colour. - Website needs to be sleek, chic and masculine.- Colour Palette - Grey/ Black/ White - Same visiual journey as Brantley website- Required areas within the sit include - About Us / Our Work / Contact Page

Target Market(s)

Luxury
Men

Number of Pages Required

2 page

Font styles to use
Sans Serif

Colors
e8e8e8
757575
1b1b1b
000000
9d9d9d
cbcbcb
f5f5f5

Requirements
Must have
• Complimentary of this site - https://www.brantleyhq.example/brantley-nu-staging
Should not have
• Colour

```html
<!DOCTYPE html>
<html lang="en">
<head>
<meta charset="utf-8">
<title>Motor Vault — Part of the Brantley Group</title>
<link rel="stylesheet" href="https://fonts.googleapis.com/css2?family=Open+Sans:wght@600;700&family=Poppins:wght@300;400;500&display=swap">
<style>
  :root {
    --white: #ffffff;
    --paper: #f5f5f5;
    --mist: #e8e8e8;
    --silver: #cbcbcb;
    --ash: #9d9d9d;
    --slate: #757575;
    --coal: #1b1b1b;
    --black: #000000;
    --body: "Poppins", sans-serif;
    --head: "Open Sans", sans-serif;
  }
  * { box-sizing: border-box; margin: 0; padding: 0; }
  html, body { width: 1200px; height: 2311px; overflow: hidden; }
  body { position: relative; font-family: var(--body); background: var(--white); color: var(--coal); }

  /* Hero */
  .hero {
    position: absolute; left: 0; top: 0; width: 1200px; height: 600px;
    background:
      radial-gradient(ellipse 180px 150px at 50% 42%, rgba(190,190,190,.55) 0%, rgba(120,120,120,.25) 60%, rgba(0,0,0,0) 100%),
      linear-gradient(90deg, #141414 0%, #3a3a3a 14%, #262626 24%, #4a4a4a 38%, #5a5a5a 50%, #4a4a4a 62%, #262626 76%, #3a3a3a 86%, #141414 100%);
  }
  .hero::after {
    content: ""; position: absolute; inset: 0;
    background: linear-gradient(rgba(0,0,0,.35) 0%, rgba(0,0,0,0) 30%, rgba(0,0,0,0) 60%, rgba(0,0,0,.55) 100%);
  }
  .site-nav {
    position: absolute; left: 0; top: 34px; width: 1200px; height: 76px; z-index: 2;
    background: linear-gradient(#2a2a2a, #0c0c0c);
  }
  .brand { position: absolute; display: flex; align-items: center; gap: 8px; color: var(--white); }
  .brand-mark { width: 22px; height: 22px; background: var(--white); }
  .brand-text { display: flex; flex-direction: column; line-height: 1; }
  .brand-name { font-family: var(--body); font-weight: 400; font-size: 31px; letter-spacing: 1px; }
  .brand-sub { font-size: 6px; letter-spacing: 1px; color: var(--ash); margin-top: 3px; }
  .site-nav .brand { left: 112px; top: 20px; }
  .nav-links { position: absolute; right: 118px; top: 28px; display: flex; gap: 46px; list-style: none; }
  .nav-links li { color: var(--white); font-size: 15px; }

  .hero-copy { position: absolute; left: 0; top: 238px; width: 1200px; text-align: center; color: var(--white); z-index: 2; }
  .hero-kicker { font-family: var(--head); font-weight: 700; font-size: 15px; }
  .hero-title { font-family: var(--head); font-weight: 600; font-size: 62px; line-height: 1; margin-top: 6px; }
  .hero-tagline { font-family: var(--head); font-weight: 700; font-size: 21px; margin-top: 10px; }
  .hero-lede { font-size: 15px; line-height: 31px; margin-top: 4px; }
  .hero-arrow { position: absolute; top: 314px; z-index: 2; }
  .hero-arrow.prev { left: 62px; }
  .hero-arrow.next { right: 62px; }

  /* About */
  .about { position: absolute; left: 0; top: 600px; width: 1200px; height: 493px; background: var(--mist); }
  .about h2 { position: absolute; left: 112px; top: 92px; font-family: var(--head); font-weight: 600; font-size: 34px; color: var(--black); }
  .about-text { position: absolute; left: 112px; top: 168px; width: 585px; font-size: 14.5px; line-height: 31px; color: #5e5e5e; }
  .about-text p + p { margin-top: 10px; }
  .about-glow {
    position: absolute; left: 868px; top: 40px; width: 120px; height: 90px; border-radius: 50%;
    background: radial-gradient(ellipse, rgba(255,255,255,.9) 0%, rgba(255,255,255,0) 70%);
  }
  .about-photo {
    position: absolute; left: 758px; top: 103px; width: 340px; height: 340px; border-radius: 50%;
    border: 8px solid var(--ash);
    background:
      linear-gradient(115deg, rgba(255,255,255,0) 28%, rgba(230,230,230,.55) 36%, rgba(255,255,255,0) 44%),
      radial-gradient(circle at 70% 70%, #6e6e6e 0%, rgba(0,0,0,0) 30%),
      linear-gradient(160deg, #4a4a4a 0%, #242424 45%, #101010 100%);
  }

  /* Works */
  .works { position: absolute; left: 0; top: 1093px; width: 1200px; height: 827px; background: var(--white); }
  .works h2 { position: absolute; left: 0; top: 78px; width: 1200px; text-align: center; font-family: var(--head); font-weight: 600; font-size: 34px; color: var(--black); }
  .work-tile {
    position: absolute; width: 312px; height: 260px; display: flex; align-items: center; justify-content: center;
    background: linear-gradient(150deg, #5d5d5d 0%, #2b2b2b 55%, #0d0d0d 100%);
  }
  .work-tile.shell { background: linear-gradient(135deg, #8a8a8a 0%, #4d4d4d 40%, #6a6a6a 70%, #2a2a2a 100%); }
  .work-tile.basements { background: linear-gradient(180deg, #1c1c1c 0%, #3e3e3e 40%, #5a5a5a 70%, #2e2e2e 100%); }
  .work-tile.interiors { background: radial-gradient(ellipse at 20% 20%, #8c8c8c 0%, #3a3a3a 45%, #0e0e0e 100%); }
  .work-tile.accusamus { background: linear-gradient(180deg, #3a3a3a 0%, #1a1a1a 45%, #4a4a4a 80%, #141414 100%); }
  .work-tile.odio { background: linear-gradient(160deg, #6a6a6a 0%, #2e2e2e 45%, #575757 75%, #121212 100%); }
  .work-tile.ducimus { background: radial-gradient(ellipse at 55% 80%, #9a9a9a 0%, #3c3c3c 40%, #141414 100%); }
  .work-tile .corner { position: absolute; }
  .work-tile .corner.tl { left: 14px; top: 18px; width: 82px; height: 44px; border-left: 2px solid var(--white); border-top: 2px solid var(--white); }
  .work-tile .corner.br { right: 14px; bottom: 10px; width: 82px; height: 64px; border-right: 2px solid var(--white); border-bottom: 2px solid var(--white); }
  .work-label { position: relative; font-family: var(--head); font-weight: 700; font-size: 20px; color: var(--white); text-shadow: 0 1px 3px rgba(0,0,0,.5); }

  /* Footer */
  .site-footer { position: absolute; left: 0; top: 1920px; width: 1200px; height: 391px; background: linear-gradient(160deg, #181818, #0b0b0b 60%, #141414); color: var(--white); }
  .site-footer .brand { left: 0; width: 1200px; top: 63px; justify-content: center; }
  .newsletter { position: absolute; left: 396px; top: 138px; width: 408px; height: 43px; border: 2px solid var(--white); display: flex; }
  .newsletter .field { flex: 1; padding: 0 12px; display: flex; align-items: center; font-size: 15px; color: var(--ash); border-right: 2px solid var(--white); }
  .newsletter .submit { width: 90px; display: flex; align-items: center; justify-content: center; font-size: 15px; }
  .contact-row { position: absolute; left: 0; top: 212px; width: 1200px; display: flex; justify-content: center; gap: 20px; font-size: 15px; }
  .contact-row span { display: flex; align-items: center; gap: 8px; }
  .social { position: absolute; left: 0; top: 182px; width: 1200px; display: flex; justify-content: center; gap: 17px; list-style: none; margin-top: 82px; }
  .social li { width: 20px; height: 20px; border-radius: 50%; border: 2px solid var(--white); }
  .copyright { position: absolute; left: 0; top: 311px; width: 1200px; text-align: center; font-size: 15px; }
</style>
</head>
<body>

<header class="hero" role="img" aria-label="Photograph of a long concrete basement corridor under construction">
  <nav class="site-nav">
    <div class="brand">
      <span class="brand-mark"></span>
      <span class="brand-text"><span class="brand-name">MOTOR VAULT</span><span class="brand-sub">PART OF THE BRANTLEY GROUP</span></span>
    </div>
    <ul class="nav-links">
      <li>Welcome</li><li>About Us</li><li>Our Work</li><li>Contact</li>
    </ul>
  </nav>
  <div class="hero-copy">
    <p class="hero-kicker">WELCOME TO</p>
    <h1 class="hero-title">MOTOR VAULT</h1>
    <p class="hero-tagline">LONDON'S ORIGINAL BASEMENT CONTRACTOR</p>
    <p class="hero-lede">At vero eos et accusamus et iusto odio dignissimos ducimus qui blanditiis<br>praesentium voluptatum deleniti atque molestias</p>
  </div>
  <svg class="hero-arrow prev" width="28" height="44" viewBox="0 0 28 44"><path d="M24 4 L6 22 L24 40" fill="none" stroke="#9d9d9d" stroke-width="5"/></svg>
  <svg class="hero-arrow next" width="28" height="44" viewBox="0 0 28 44"><path d="M4 4 L22 22 L4 40" fill="none" stroke="#9d9d9d" stroke-width="5"/></svg>
</header>

<section class="about">
  <h2>ABOUT US</h2>
  <div class="about-text">
    <p>Today, Motor Vault designs and builds hundreds of basements in central London and the home counties every year and is considered a leading authority in basement construction. Managing Director Adrian Brantley has been building basements in London for over 20 years and was instrumental in setting today's trends in basement construction.</p>
    <p>Brantley operates a dependable, financially strong and leading London construction business which has been awarded</p>
  </div>
  <div class="about-glow"></div>
  <div class="about-photo" role="img" aria-label="Photograph of a worker inside a steel-framed basement excavation lit by a shaft of light"></div>
</section>

<section class="works">
  <h2>Our Works</h2>
  <div class="work-tile shell" style="left:112px;top:170px" role="img" aria-label="Steel roof structure photograph"><span class="corner tl"></span><span class="corner br"></span><span class="work-label">SHELL &amp; CORE</span></div>
  <div class="work-tile basements" style="left:448px;top:170px" role="img" aria-label="Basement excavation site photograph"><span class="corner tl"></span><span class="corner br"></span><span class="work-label">BASEMENTS</span></div>
  <div class="work-tile interiors" style="left:787px;top:170px" role="img" aria-label="Interior construction photograph"><span class="corner tl"></span><span class="corner br"></span><span class="work-label">INTERIORS</span></div>
  <div class="work-tile accusamus" style="left:112px;top:473px" role="img" aria-label="Excavator in a basement photograph"><span class="corner tl"></span><span class="corner br"></span><span class="work-label">ACCUSAMUS ET IUSTO</span></div>
  <div class="work-tile odio" style="left:448px;top:473px" role="img" aria-label="Underground garage photograph"><span class="corner tl"></span><span class="corner br"></span><span class="work-label">ODIO DIGNISSIMOS</span></div>
  <div class="work-tile ducimus" style="left:787px;top:473px" role="img" aria-label="Welding sparks on site photograph"><span class="corner tl"></span><span class="corner br"></span><span class="work-label">DUCIMUS QUI</span></div>
</section>

<footer class="site-footer">
  <div class="brand">
    <span class="brand-mark"></span>
    <span class="brand-text"><span class="brand-name">MOTOR VAULT</span><span class="brand-sub">PART OF THE BRANTLEY GROUP</span></span>
  </div>
  <div class="newsletter"><span class="field">Email</span><span class="submit">submit</span></div>
  <div class="contact-row">
    <span><svg width="12" height="16" viewBox="0 0 12 16"><path d="M6 0C2.7 0 0 2.6 0 5.8 0 10 6 16 6 16s6-6 6-10.2C12 2.6 9.3 0 6 0zm0 8a2.2 2.2 0 1 1 0-4.4A2.2 2.2 0 0 1 6 8z" fill="#fff"/></svg>Sed ut perspiciatis unde omnis</span>
    <span><svg width="14" height="14" viewBox="0 0 14 14"><path d="M3 0l2.5 3.3-1.4 1.8c.9 1.8 2.4 3.3 4.2 4.2l1.8-1.4L14 10.5 12 14C5.4 14 0 8.6 0 2z" fill="#fff"/></svg>8905550142</span>
    <span><svg width="16" height="12" viewBox="0 0 16 12"><rect width="16" height="12" rx="1" fill="#fff"/><path d="M1 1l7 5 7-5" fill="none" stroke="#111" stroke-width="1.4"/></svg>info@motorvault.example</span>
  </div>
  <ul class="social" aria-label="Social links">
    <li aria-label="Social link"></li><li aria-label="Social link"></li><li aria-label="Social link"></li><li aria-label="Social link"></li>
  </ul>
  <p class="copyright">Copyright © Motor Vault 2018. Terms And Conditions | Privacy Policy</p>
</footer>

</body>
</html>
```